Delworth Consulting Updated Web design

We need to update our website, reconfigure some pages, have the availability for people to register for courses and integrate with our on-line store. It must be something were a novice (like myself) can update classes as they are changed almost daily. We offer training to Police, Fire and 911 Operators so it should be themed as such. See current site at delworthconsulting.example It should have a clear POLICE, FIRE, 911 DISPATCH on home screen to bring visitors to their area and we will need subcategory of pages from there. See uploaded site map for details. I will need guidance on how to get your design up and live, small operation and none of us are tech savvy.

Target Market(s)

Police Officers and Departments, Fire Departments and Dispatch 911

Coding

Coded - Design and coding required

Number of Pages Required

5+ page

Requirements
Must have
• See uploaded word document with site map

```html
<!DOCTYPE html>
<html lang="en">
<head>
<meta charset="utf-8">
<title>Delworth Consulting</title>
<link href="https://fonts.googleapis.com/css2?family=Barlow+Condensed:wght@500;600;700&family=Barlow:wght@400;500&family=Roboto:wght@400&display=swap" rel="stylesheet">
<style>
:root{
  --navy:#0c1a5e;
  --navy-deep:#0a1352;
  --gold:#f8bb1c;
  --gold-dark:#f2ad00;
  --ink:#4a4a4a;
  --light:#f4f4f4;
  --white:#ffffff;
}
*{margin:0;padding:0;box-sizing:border-box}
html,body{width:1200px;height:3807px;overflow:hidden}
body{position:relative;background:var(--white);font-family:"Barlow",sans-serif;color:var(--ink)}
.abs{position:absolute}

/* header */
.brand{left:111px;top:58px;width:200px;font-family:"Barlow Condensed",sans-serif;font-weight:700;font-size:30px;line-height:1.05;color:var(--navy);text-transform:uppercase;z-index:3}
.call-icon{left:840px;top:33px;width:64px;height:64px;border-radius:50%;background:var(--navy);display:flex;align-items:center;justify-content:center}
.call-text{left:910px;top:50px;font-family:"Barlow Condensed",sans-serif;font-weight:600;font-size:22px;color:#444}
.navbar{left:0;top:127px;width:1200px;height:68px;background:var(--gold);border-bottom:3px solid #e9a800}
.nav-item{top:127px;height:68px;display:flex;align-items:center;font-family:"Barlow Condensed",sans-serif;font-weight:600;font-size:19px;color:var(--white);text-transform:uppercase}
.nav-item.active{background:var(--navy);justify-content:center}

/* hero */
.hero{left:0;top:195px;width:1200px;height:733px;background:radial-gradient(ellipse at 60% 40%,#4a4c52 0%,#2a2c33 45%,#16181d 100%)}
.hero-title{left:0;top:605px;width:1200px;text-align:center;font-family:"Barlow Condensed",sans-serif;font-weight:700;font-size:56px;color:var(--gold)}
.hero-sub{left:0;top:680px;width:1200px;text-align:center;font-family:"Barlow Condensed",sans-serif;font-weight:500;font-size:34px;color:var(--white)}
.btn-gold{background:var(--gold);color:var(--white);font-family:"Barlow Condensed",sans-serif;font-weight:600;display:flex;align-items:center;justify-content:center;text-transform:uppercase}
.hero-btn{left:507px;top:745px;width:188px;height:60px;font-size:22px}

/* about */
.about-photo{left:111px;top:1001px;width:525px;height:518px;background:linear-gradient(135deg,#bdbdbd,#6c6c6c 55%,#2a2a2a)}
.about-box{left:559px;top:1030px;width:530px;height:458px;background:var(--white);border:1px solid #e6e6e6}
.about-inner{left:568px;top:1039px;width:512px;height:440px;border:1.5px solid var(--gold)}
.about-h{left:610px;top:1078px;font-family:"Barlow Condensed",sans-serif;font-weight:700;font-size:42px;color:var(--navy)}
.about-sub{left:610px;top:1126px;font-family:"Barlow Condensed",sans-serif;font-weight:700;font-size:35px;color:var(--gold)}
.about-p{left:610px;top:1183px;width:434px;font-size:16.5px;line-height:26.6px;text-align:justify;color:#555}
.btn-navy{left:610px;top:1392px;width:139px;height:49px;background:var(--navy);color:var(--white);font-family:"Barlow Condensed",sans-serif;font-weight:600;font-size:19px;display:flex;align-items:center;justify-content:center}

/* training */
.training{left:0;top:1601px;width:1200px;height:632px;background:var(--light)}
.sec-title{left:0;width:1200px;text-align:center;font-family:"Barlow Condensed",sans-serif;font-weight:700;font-size:46px;color:var(--navy)}
.sec-title span{color:var(--gold)}
.rule{left:573px;width:54px;height:3px;background:var(--gold)}
.card{top:1745px;width:235px;height:416px}
.card-img{width:235px;height:196px}
.card-body{position:absolute;left:0;top:196px;width:235px;height:220px;padding:18px 8px 0;text-align:center;color:var(--white)}
.card.gold .card-body{background:var(--gold)}
.card.navy .card-body{background:var(--navy)}
.card h3{font-family:"Barlow Condensed",sans-serif;font-weight:600;font-size:18.5px;line-height:25px;text-transform:uppercase;white-space:nowrap}
.card p{font-family:"Roboto",sans-serif;font-size:13.5px;line-height:25.5px;margin-top:6px;padding:0 14px}
.card.gold p{color:#fff7e0}
.card-btn{position:absolute;left:69px;bottom:26px;width:97px;height:34px;border:1px solid var(--white);font-family:"Barlow Condensed",sans-serif;font-size:15.5px;display:flex;align-items:center;justify-content:center;text-transform:uppercase}

/* entry */
.entry{left:0;top:2233px;width:1200px;height:591px;background:linear-gradient(90deg,#3a3a32 0%,#2d3238 45%,#1f2329 100%)}
.entry-title{left:111px;top:2400px;font-family:"Barlow Condensed",sans-serif;font-weight:600;font-size:56px;line-height:62px;color:var(--white);text-transform:uppercase}
.entry-p{left:111px;top:2536px;width:430px;font-family:"Roboto",sans-serif;font-size:14px;line-height:25.7px;color:var(--white)}
.entry-btn{left:111px;top:2635px;width:152px;height:54px;font-size:21px}

/* testimonials */
.quote-card{top:3012px;width:313px;height:330px;background:var(--white);border:1px solid #e4e4e4;text-align:center}
.quote-mark{position:absolute;left:123px;top:-27px;width:66px;height:66px;border-radius:50%;background:var(--gold);border:3px solid var(--white);box-shadow:0 0 0 1px #eee;display:flex;align-items:center;justify-content:center}
.quote-text{position:absolute;left:28px;top:60px;width:257px;font-family:"Roboto",sans-serif;font-size:13.5px;line-height:25.7px;color:#555}
.stars{position:absolute;left:0;top:255px;width:100%;text-align:center;color:var(--gold);font-size:15px;letter-spacing:2px}
.quote-name{position:absolute;left:0;top:278px;width:100%;text-align:center;font-family:"Barlow Condensed",sans-serif;font-size:19px;color:#333}

/* footer */
.footer{left:0;top:3408px;width:1200px;height:399px;background:var(--navy-deep)}
.foot-brand{left:196px;top:3506px;width:160px;text-align:center;font-family:"Barlow Condensed",sans-serif;font-weight:700;font-size:26px;line-height:1.05;color:var(--gold);text-transform:uppercase}
.vline{top:3470px;width:1px;height:125px;background:#33407a}
.foot-text{font-family:"Barlow",sans-serif;font-weight:500;font-size:14px;line-height:22.5px;color:var(--white)}
.hline{left:111px;top:3656px;width:978px;height:1px;background:#2a3672}
.foot-nav{top:3692px;font-family:"Barlow",sans-serif;font-weight:500;font-size:14px;color:var(--white);text-transform:uppercase}
.copy{left:0;top:3737px;width:1200px;text-align:center;font-family:"Barlow",sans-serif;font-weight:500;font-size:16px;color:var(--white)}
</style>
</head>
<body>

<!-- header -->
<div class="abs brand">Delworth<br>Consulting</div>
<div class="abs call-icon">
  <svg width="22" height="22" viewBox="0 0 24 24"><path fill="#fff" d="M6.6 10.8a15.1 15.1 0 0 0 6.6 6.6l2.2-2.2a1 1 0 0 1 1-.25 11.4 11.4 0 0 0 3.6.57 1 1 0 0 1 1 1V20a1 1 0 0 1-1 1A17 17 0 0 1 3 4a1 1 0 0 1 1-1h3.5a1 1 0 0 1 1 1c0 1.250.2 2.45.57 3.6a1 1 0 0 1-.25 1z"/></svg>
</div>
<div class="abs call-text">CALL US : 555.014.2290</div>

<div class="abs navbar"></div>
<div class="abs nav-item active" style="left:288px;width:90px">Home</div>
<div class="abs nav-item" style="left:398px">Police</div>
<div class="abs nav-item" style="left:489px">Fire</div>
<div class="abs nav-item" style="left:563px">911 Dispatch</div>
<div class="abs nav-item" style="left:695px">Upcoming Course List</div>
<div class="abs nav-item" style="left:896px">About Us</div>
<div class="abs nav-item" style="left:1005px">Contact Us</div>

<!-- hero -->
<div class="abs hero" role="img" aria-label="Officers training with handguns at an indoor firing range"></div>
<div class="abs hero-title">DELWORTH CONSULTING, LLC</div>
<div class="abs hero-sub">PUBLIC SAFETY PROMOTIONS, TRAINING, SELECTION &amp; MORE</div>
<div class="abs btn-gold hero-btn">Learn More</div>

<!-- about -->
<div class="abs about-photo" role="img" aria-label="Black and white photo of a uniformed police officer shaking hands with a man in a suit"></div>
<div class="abs about-box"></div>
<div class="abs about-inner"></div>
<div class="abs about-h">ABOUT US</div>
<div class="abs about-sub">ATTORNEY OWEN DELWORTH</div>
<p class="abs about-p">Owen is a Massachusetts licensed attorney and a police manager with more than 25 years of experience. &nbsp;Owen has been teaching police officers and police supervisors for many years in the area of critical incident management, policy development, police supervision, criminal law and criminal procedure. Owen enjoys teaching police officers and is improving law enforcement in the Commonwealth.</p>
<div class="abs btn-navy">READ MORE</div>

<!-- training -->
<div class="abs training"></div>
<h2 class="abs sec-title" style="top:1640px">OUR <span>TRAINING</span></h2>
<div class="abs rule" style="top:1708px"></div>

<div class="abs card gold" style="left:111px">
  <div class="card-img" role="img" aria-label="Police officers saluting at a ceremony" style="background:linear-gradient(160deg,#b08a5a,#3b3128 60%,#1d1a1a)"></div>
  <div class="card-body"><h3>Police Promotional<br>Preparation</h3><p>We have quickly become the leader in Police Promotional Preparation in Massachusetts.</p><div class="card-btn">Read More</div></div>
</div>
<div class="abs card navy" style="left:359px">
  <div class="card-img" role="img" aria-label="A police officer and a firefighter in uniform" style="background:linear-gradient(110deg,#e8e8e8,#2a2f45 40%,#c9d93a 75%,#eeeeee)"></div>
  <div class="card-body"><h3>Public Safety Employment<br>Preparation</h3><p>Exam preparation, interviewing &amp; assessment centers, career path and job search.</p><div class="card-btn">Read More</div></div>
</div>
<div class="abs card gold" style="left:607px">
  <div class="card-img" role="img" aria-label="Professionals in a meeting around a conference table" style="background:linear-gradient(170deg,#f2f2f2,#9aa0a8 55%,#4a5058)"></div>
  <div class="card-body" style="padding-top:22px"><h3>911 Training Courses</h3><p style="margin-top:2px">Advanced &amp; Specialized legal training for State, Municipal and Campus Police. Custom tailor training to the needs.</p><div class="card-btn">Read More</div></div>
</div>
<div class="abs card navy" style="left:854px">
  <div class="card-img" role="img" aria-label="Uniformed officers standing in a line on a street" style="background:linear-gradient(180deg,#c8c8c8,#3a3c44 60%,#8a8a8a)"></div>
  <div class="card-body"><h3>Law Enforcement<br>Agency Services</h3><p>Training, Entrance Promotional Exam creation &amp;administration, Assessment Centers</p><div class="card-btn">Read More</div></div>
</div>

<!-- entry examinations -->
<div class="abs entry" role="img" aria-label="Police officer with crossed arms standing in front of a patrol car at dusk"></div>
<div class="abs entry-title">Entry<br>Examinations</div>
<p class="abs entry-p">We provide the absolute best testing services to help your agency select the absolute best candidate for your needs. Our examinations are customized to the needs of each individual agency.</p>
<div class="abs btn-gold entry-btn">Read More</div>

<!-- testimonials -->
<h2 class="abs sec-title" style="top:2876px">CLIENTS <span>TESTIMONIALS</span></h2>
<div class="abs rule" style="top:2943px"></div>

<div class="abs quote-card" style="left:112px">
  <div class="quote-mark"><svg width="24" height="20" viewBox="0 0 24 20"><path fill="#fff" d="M0 20V11C0 4 3 1 9 0l1 3C6 4 5 6 5 9h5v11zm14 0V11c0-7 3-10 9-11l1 3c-4 1-5 3-5 6h5v11z"/></svg></div>
  <p class="quote-text">Hey Owen, I just wanted to let you know that I was lucky enough to get promoted to Chief last week here in XXXXX. Part of the reason I was able to do that was because of you. I am not sending this for any other reason but to say thanks and if future please feel free to call.</p>
  <div class="stars">★★★★★</div><div class="quote-name">Jhon Smith</div>
</div>
<div class="abs quote-card" style="left:444px">
  <div class="quote-mark"><svg width="24" height="20" viewBox="0 0 24 20"><path fill="#fff" d="M0 20V11C0 4 3 1 9 0l1 3C6 4 5 6 5 9h5v11zm14 0V11c0-7 3-10 9-11l1 3c-4 1-5 3-5 6h5v11z"/></svg></div>
  <p class="quote-text">Hi Owen, I followed the personal trainer religiously every week, utilized study guides, edge outlines, &amp; flashcards…One of only two in (a large agency) who passed the LT. exam. No question about it the program works, without program I one on LT. exam. Thank you again.</p>
  <div class="stars">★★★★★</div><div class="quote-name">Jhon Smith</div>
</div>
<div class="abs quote-card" style="left:776px">
  <div class="quote-mark"><svg width="24" height="20" viewBox="0 0 24 20"><path fill="#fff" d="M0 20V11C0 4 3 1 9 0l1 3C6 4 5 6 5 9h5v11zm14 0V11c0-7 3-10 9-11l1 3c-4 1-5 3-5 6h5v11z"/></svg></div>
  <p class="quote-text">Hello Owen, Wanted to send out an update from the XXXXXX Police Department. I have been a Delworth Consulting customer and fan for the past few tests. The efforts have paid off as I was promoted to sergeant last night. Your Can't thank you enough. Be safe.</p>
  <div class="stars">★★★★★</div><div class="quote-name">Jhon Smith</div>
</div>

<!-- footer -->
<div class="abs footer"></div>
<div class="abs foot-brand">Delworth<br>Consulting</div>
<div class="abs vline" style="left:445px"></div>
<div class="abs vline" style="left:776px"></div>

<svg class="abs" style="left:491px;top:3488px" width="18" height="24" viewBox="0 0 18 24"><path fill="none" stroke="#fff" stroke-width="1.6" d="M9 23s7.5-8.5 7.5-14A7.5 7.5 0 0 0 1.5 9C1.5 14.5 9 23 9 23z"/><circle cx="9" cy="9" r="2.8" fill="none" stroke="#fff" stroke-width="1.6"/></svg>
<div class="abs foot-text" style="left:531px;top:3481px">Delworth Consulting<br>P.O. Box 118 Fairbrook,<br>MA 01990</div>
<div class="abs" style="left:530px;top:3557px;width:42px;height:42px;border:2px solid #fff;border-radius:50%"></div>

<svg class="abs" style="left:830px;top:3490px" width="20" height="20" viewBox="0 0 24 24"><path fill="none" stroke="#fff" stroke-width="1.5" d="M6.6 10.8a15.1 15.1 0 0 0 6.6 6.6l2.2-2.2a1 1 0 0 1 1-.25 11.4 11.4 0 0 0 3.6.57 1 1 0 0 1 1 1V20a1 1 0 0 1-1 1A17 17 0 0 1 3 4a1 1 0 0 1 1-1h3.5a1 1 0 0 1 1 1c0 1.25.2 2.45.57 3.6a1 1 0 0 1-.25 1z"/></svg>
<div class="abs foot-text" style="left:868px;top:3481px">Phone:<br>(555) 014-2290</div>
<svg class="abs" style="left:830px;top:3561px" width="22" height="16" viewBox="0 0 22 16"><rect x="1" y="1" width="20" height="14" fill="none" stroke="#fff" stroke-width="1.5"/><path d="M1 1l10 8 10-8" fill="none" stroke="#fff" stroke-width="1.5"/></svg>
<div class="abs foot-text" style="left:870px;top:3550px">Email:<br>info@delworthconsulting.example</div>

<div class="abs hline"></div>
<div class="abs foot-nav" style="left:300px">Home</div>
<div class="abs foot-nav" style="left:372px">Police</div>
<div class="abs foot-nav" style="left:455px">Fire</div>
<div class="abs foot-nav" style="left:520px">911 Dispatch</div>
<div class="abs foot-nav" style="left:641px">Upcoming Course List</div>
<div class="abs foot-nav" style="left:834px">About Us</div>
<div class="abs copy">Delworth Consulting © 2021.All Rights Reserved.</div>

</body>
</html>
```